Poster Required for Cafe to promote Catering

I would like a Poster made to advertise that our business does catering.
On the poster we would like it to say:

Did you know that Sunny Ladle does Catering?
We offer Breakfast, Lunch, Morning and Afternoon Tea Options
Come instore to enquire

At the bottom of the flyer, can you please put the contact details:
Phone 0487 602 914
Email tam@sunnyladlecanteen.com

Poster Size A3

I have attached our logo and menu's so you can get a feel for what we like.

Target Market(s)

Hospital Staff: Doctors, Nurses, Admin

Industry/Entity Type

Hospitality

Requirements
Nice to have
• Some pictures of catering. Eg. Gourmet Sandwiches, Sliders
• You could check our instagram page for ideas on what we do..
• @snyladle_qld

```html
<!DOCTYPE html>
<html lang="en">
<head>
<meta charset="utf-8">
<title>Sunny Ladle Catering Poster</title>
<link rel="stylesheet" href="https://fonts.googleapis.com/css2?family=Raleway:ital,wght@0,200;0,400;1,800&family=Oswald:wght@400&family=Arimo&display=swap">
<style>
  :root {
    --bg-dark: #1c1c1c;
    --bg-mid: #2e2e2e;
    --ink-light: #ffffff;
    --accent-yellow: #fdf8a3;
    --accent-yellow-text: #fbf291;
    --ink-dark: #3b3232;
  }
  html, body {
    margin: 0;
    padding: 0;
    overflow: hidden;
    background: var(--bg-dark);
  }
  .poster {
    position: relative;
    width: 849px;
    height: 1200px;
    overflow: hidden;
    background: radial-gradient(ellipse at 50% 40%, var(--bg-mid) 0%, var(--bg-dark) 75%);
  }
  .poster svg { display: block; }
  .thin { font-family: "Raleway", sans-serif; font-weight: 200; fill: var(--ink-light); }
  .regular { font-family: "Raleway", sans-serif; font-weight: 400; fill: var(--ink-light); }
  .ribbon-word { font-family: "Raleway", sans-serif; font-weight: 800; font-style: italic; fill: var(--accent-yellow-text); }
  .cta { font-family: "Oswald", sans-serif; font-weight: 400; fill: var(--ink-dark); }
  .contact { font-family: "Arimo", sans-serif; fill: var(--ink-light); font-size: 17px; }
  .frame { fill: none; stroke: var(--ink-light); stroke-width: 2; }
  .ribbon { fill: var(--bg-dark); stroke: var(--ink-light); stroke-width: 2.5; }
  .cta-band { fill: var(--accent-yellow); }
</style>
</head>
<body>
<main class="poster">
  <svg width="849" height="1200" viewBox="0 0 849 1200" xmlns="http://www.w3.org/2000/svg">
    <!-- Headline -->
    <text class="thin headline" x="76" y="184" font-size="64">Did you know</text>
    <text x="76" y="263" font-size="64">
      <tspan class="thin">the </tspan><tspan class="regular">SUNNY LADLE</tspan>
    </text>
    <text class="thin" x="76" y="340" font-size="64">does</text>

    <!-- Catering ribbon -->
    <polygon class="ribbon" points="243,293 643,293 623,323 643,354 243,354 263,323"/>
    <text class="ribbon-word" x="443" y="340" font-size="48" text-anchor="middle">CATERING</text>
    <text class="thin" x="661" y="340" font-size="64">?</text>

    <!-- Offer block -->
    <text class="thin" x="78" y="505" font-size="47">We offer</text>
    <polyline class="frame" points="283,505 783,505 783,640"/>
    <text class="regular" x="80" y="578" font-size="70" textLength="678" lengthAdjust="spacingAndGlyphs">BREAKFAST▪LUNCH</text>
    <text class="thin" x="80" y="633" font-size="46" textLength="685" lengthAdjust="spacingAndGlyphs">MORNING &amp; AFTERNOON TEA</text>
    <text class="thin" x="765" y="675" font-size="32" text-anchor="end">OPTIONS</text>

    <!-- Lower frame -->
    <polyline class="frame" points="597,650 86,650 86,1040 205,1040"/>
    <polyline class="frame" points="765,683 765,1040 647,1040"/>

    <!-- Call to action -->
    <rect class="cta-band" x="86" y="742" width="679" height="212"/>
    <text class="cta" x="425" y="818" font-size="38" text-anchor="middle">COME INSTORE  TO</text>
    <text class="cta" x="425" y="901" font-size="90" text-anchor="middle" textLength="307" lengthAdjust="spacingAndGlyphs">ENQUIRE</text>

    <!-- Contact ribbon -->
    <polygon class="ribbon" points="205,1005 647,1005 630,1048 647,1092 205,1092 222,1048"/>
    <text class="contact" x="426" y="1040" text-anchor="middle">Ph:0487 602 914</text>
    <text class="contact" x="426" y="1069" text-anchor="middle">Email: tam@sunnyladlecanteen.com</text>
  </svg>
</main>
</body>
</html>
```